Pelkman Agency (http://pa.quorvexstudio.com/)

We are looking for a similar design to what we have, but more professional looking and cleaned up with links and logo that is not so grainy looking. We are an independent insurance agency marketing to personal and commercial clients. We offer all commercial lines markets and all personal lines. We target excavators, landscapers, restaurants, golf courses, contractors. Please look at http://pa.quorvexstudio.com/ which we had designed but do not like it, it will give you an idea of what we are looking for.

Target Market(s)

Commercial and personal insurance. All business products and all personal (homeowners, auto, antique auto, umbrella)

Industry/Entity Type

It Professional

Logo Text

Knowledge Building Your Assurance

Number of Pages Required

5+ page

Colors
000000
848484
0255a3

```html
<!DOCTYPE html>
<html lang="en">
<head>
<meta charset="utf-8">
<title>Pelkman Agency – FAQs</title>
<link rel="stylesheet" href="https://fonts.googleapis.com/css2?family=Open+Sans:wght@300;400;600;700&display=swap">
<style>
:root{
  --blue:#0f7acb;
  --ink:#333;
  --muted:#8a8f94;
  --line:#e3e3e3;
  --footer:#363739;
  --footer-deep:#2d2e30;
  --footer-text:#d7d7d7;
  --icon:#c4c6c8;
}
*{margin:0;padding:0;box-sizing:border-box}
html,body{width:1200px;height:929px;overflow:hidden;background:#fff}
body{font-family:"Open Sans",Arial,sans-serif;color:var(--ink);position:relative}
.abs{position:absolute;white-space:nowrap}
a{color:inherit;text-decoration:none}

.topbar{position:absolute;left:0;top:0;width:1200px;height:31px;border-bottom:1px solid #eee}
.topbar .contact{left:87px;top:9px;font-size:10px;color:#666}
.topbar .contact .mail{font-size:11.5px;color:#888;margin-left:4px}
.topbar .social span{position:absolute;top:10px;width:13px;height:13px;border-radius:50%;background:#cfd1d3}
.topbar .social span.on{background:var(--blue)}
.topbar .social-mark{position:absolute;left:1078px;top:30px;width:38px;height:3px;background:var(--blue)}

.header{position:absolute;left:0;top:32px;width:1200px;height:80px}
.brand{left:87px;top:21px;font-size:27px;color:#333;letter-spacing:.2px}
.nav a{position:absolute;top:31px;font-size:13.5px;color:#333}
.nav a.more{color:var(--blue)}

.band{position:absolute;left:0;top:112px;width:1200px;height:363px;
  background:linear-gradient(#eeeeee 0,#f6f6f6 90px,#fff 250px)}

.dropdown{position:absolute;left:973px;top:112px;width:147px;height:68px;background:#fff;
  border-top:3px solid var(--blue);box-shadow:0 2px 6px rgba(0,0,0,.08);z-index:3}
.dropdown div{height:32px;line-height:32px;padding-left:20px;font-size:11.5px;color:#8a8f94}
.dropdown .active{background:#f5f5f5}

.page-title{left:87px;top:155px;font-size:22px;color:var(--blue);font-weight:400}
.crumbs{left:155px;top:163px;font-size:11px;color:#888}
.crumbs a{text-decoration:underline}
.crumbs .sep{margin:0 9px}
.search{position:absolute;left:843px;top:154px;width:272px;height:30px;background:#fff;border:1px solid #e2e2e2;
  font-size:11.5px;color:#a8a8a8;padding:8px 8px}
.search-bar{position:absolute;left:1080px;top:181px;width:35px;height:3px;background:var(--blue)}
.title-rule{position:absolute;left:86px;top:202px;width:1029px;height:1px;background:var(--line)}
.title-rule i{position:absolute;left:0;top:-2px;width:79px;height:3px;background:var(--blue)}

.faq-list{position:absolute;left:86px;top:256px;width:325px;border:1px solid #dedede;background:#fff}
.faq-list li{list-style:none;position:relative;padding:12px 17px;font-size:11.3px;font-weight:300;color:#777;
  line-height:17.5px;border-top:1px solid #dedede;min-height:40px}
.faq-list li:first-child{border-top:0}
.faq-list li.current{color:var(--blue);background:#f4f4f4}
.faq-list li.current svg{position:absolute;right:-12px;top:-1px}

.answer-title{left:453px;top:248px;font-size:26px;font-weight:300;color:#333}
.answer-rule{position:absolute;left:456px;top:300px;width:659px;height:1px;background:var(--line)}
.answer-rule i{position:absolute;left:0;top:-1px;width:66px;height:3px;background:var(--blue)}
.answer{position:absolute;left:455px;top:332px;width:662px;font-size:11.4px;line-height:17.5px;color:#7a8590}

.footer{position:absolute;left:0;top:475px;width:1200px;height:386px;background:var(--footer);color:var(--footer-text)}
.footer .brand-foot{left:85px;top:58px;font-size:27px;color:#fff}
.footer h4{position:absolute;top:65px;font-size:13px;font-weight:700;color:#fff;letter-spacing:.2px}
.footer .txt{position:absolute;font-size:11.5px;line-height:19.3px;color:var(--footer-text);white-space:nowrap}
.footer .date{position:absolute;font-size:9.5px;color:#3ca0ee}
.footer .chev{position:absolute;font-size:11px;color:#ddd}
.footer .ico{position:absolute}
.footer .link{color:#fff}
.newsletter-input{position:absolute;left:858px;top:160px;width:157px;height:26px;background:#eaeaea;
  font-size:11.5px;color:#9a9a9a;padding:5px 10px}
.newsletter-btn{position:absolute;left:1015px;top:160px;width:77px;height:26px;background:var(--blue);
  color:#fff;font-size:11.5px;text-align:center;line-height:26px}
.footer .social span{position:absolute;top:253px;width:22px;height:22px;border-radius:50%;background:#5a5c5f}
.footer .social span.on{background:var(--blue)}

.bottombar{position:absolute;left:0;top:861px;width:1200px;height:68px;background:var(--footer-deep)}
.bottombar .copy{left:87px;top:27px;font-size:11px;color:#ccc}
.bottombar .menu a{position:absolute;top:27px;font-size:11px;color:#ccc}
</style>
</head>
<body>

<div class="topbar">
  <div class="abs contact">Call Us Today!&nbsp; 1-888-555-0147 &nbsp;|&nbsp; <span class="mail">admin@pelkmanagency.com</span></div>
  <div class="social" aria-label="Social links">
    <span class="on" style="left:961px"></span>
    <span style="left:995px"></span>
    <span style="left:1030px"></span>
    <span style="left:1064px"></span>
    <span style="left:1098px"></span>
  </div>
  <div class="social-mark"></div>
</div>

<header class="header">
  <div class="abs brand">Pelkman Agency</div>
  <nav class="nav">
    <a style="left:510px">Home</a>
    <a style="left:574px">Personal Insurance</a>
    <a style="left:732px">Business Insurance</a>
    <a style="left:890px">About Us</a>
    <a style="left:985px">Contact Us</a>
    <a class="more" style="left:1080px">More</a>
  </nav>
</header>

<div class="band"></div>

<div class="dropdown">
  <div>Our Staff</div>
  <div class="active">FAQ</div>
</div>

<h1 class="abs page-title">FAQs</h1>
<div class="abs crumbs"><a>Home</a><span class="sep">›</span><a>FAQs</a></div>
<div class="search">To search enter keywords</div>
<div class="search-bar"></div>
<div class="title-rule"><i></i></div>

<ul class="faq-list">
  <li>What types of insurance do you offer?</li>
  <li class="current">Why should I choose Pelkman Agency?
    <svg width="12" height="42" viewBox="0 0 12 42"><path d="M0 0 L11 21 L0 42" fill="#f4f4f4" stroke="#dedede"/></svg>
  </li>
  <li>Do I have to work with a different agent for each type of insurance I need with you?</li>
</ul>

<h2 class="abs answer-title">Why should I choose Pelkman Agency?</h2>
<div class="answer-rule"><i></i></div>
<p class="answer">The main reasons are that we will work for you instead of for a major insurance company, because we have a track record of speed of response and fair settlements and that we are very accessible with early and evening hours that are very popular with our customers.</p>

<footer class="footer">
  <div class="abs brand-foot">Pelkman Agency</div>
  <div class="txt" style="left:87px;top:114px">Your Slofan Or short Description<br>Goes Here</div>

  <svg class="ico" style="left:87px;top:177px" width="10" height="14" viewBox="0 0 10 14"><path d="M5 0a5 5 0 0 1 5 5c0 4-5 9-5 9S0 9 0 5a5 5 0 0 1 5-5z" fill="#aaa"/><circle cx="5" cy="5" r="2" fill="#363739"/></svg>
  <div class="txt" style="left:112px;top:176px">Pelkman Agency<br>PO Box 204<br>12 Harbor Lane<br>Fairhollow, NJ 08999<br>Phone: (609) 555-0183<br>Fax: (609) 555-0126</div>
  <svg class="ico" style="left:86px;top:254px" width="12" height="12" viewBox="0 0 12 12"><path d="M2.5 1l2 2.5-1.2 1.2c.8 1.6 2 2.8 3.6 3.6L8.1 7l2.5 2-1.2 2C5 11 1 7 1 2.6z" fill="#aaa"/></svg>
  <svg class="ico" style="left:86px;top:273px" width="13" height="12" viewBox="0 0 13 12"><rect x="3" y="0" width="7" height="3" fill="#aaa"/><rect x="0" y="4" width="13" height="5" rx="1" fill="#aaa"/><rect x="3" y="8" width="7" height="4" fill="#aaa"/></svg>
  <svg class="ico" style="left:86px;top:316px" width="13" height="10" viewBox="0 0 13 10"><rect width="13" height="10" rx="1" fill="#aaa"/><path d="M0 1l6.5 5L13 1" stroke="#363739" fill="none"/></svg>
  <div class="txt" style="left:112px;top:311px">admin@pelkmanagency.com</div>

  <h4 style="left:343px">RECENT POSTS</h4>
  <span class="chev" style="left:343px;top:118px">›</span>
  <div class="txt link" style="left:357px;top:114px">Consecte tur adipiscing elit ut eunt</div>
  <div class="date" style="left:357px;top:135px">3 days ago</div>
  <span class="chev" style="left:343px;top:171px">›</span>
  <div class="txt link" style="left:357px;top:167px">Fusce vel tempus augue nunc</div>
  <div class="date" style="left:357px;top:188px">5 days ago</div>
  <span class="chev" style="left:343px;top:224px">›</span>
  <div class="txt link" style="left:357px;top:220px">Lorem nulla, vitae eleifend leo tincidunt</div>
  <div class="date" style="left:357px;top:241px">7 days ago</div>

  <h4 style="left:600px">RECENT TWEETS</h4>
  <span class="chev" style="left:600px;top:118px">›</span>
  <div class="txt" style="left:614px;top:114px">Integer iaculis egestas odio, vel dictum<br>turpis placerat id. Pellentesque semper<br>nisl eget: <span class="link">pa.link/Qv7rTm2</span></div>
  <div class="date" style="left:614px;top:180px">2 days ago</div>
  <span class="chev" style="left:600px;top:224px">›</span>
  <div class="txt" style="left:614px;top:220px">Curabitur consequat tortor ut eros posu<br>ere rutrum donec metus nisl, dictum vita<br>fermentum: <span class="link">pa.link/Qv7rTm2</span></div>
  <div class="date" style="left:614px;top:285px">6 days ago</div>

  <h4 style="left:857px">NEWSLETTER</h4>
  <div class="txt" style="left:858px;top:114px">Get The latest News!</div>
  <div class="newsletter-input">Email Address</div>
  <div class="newsletter-btn">Subscribe</div>
  <h4 style="left:857px;top:222px">SOCIAL MEDIA</h4>
  <div class="social" aria-label="Social media links">
    <span class="on" style="left:854px"></span>
    <span style="left:900px"></span>
    <span style="left:948px"></span>
    <span style="left:996px"></span>
    <span style="left:1044px"></span>
  </div>
</footer>

<div class="bottombar">
  <div class="abs copy">Copyright 2015 Pelkman Agency | All Rights Reserved</div>
  <nav class="menu">
    <a style="left:583px">Home</a>
    <a style="left:647px">Personal Insurance</a>
    <a style="left:773px">Business Insurance</a>
    <a style="left:900px">Service Center</a>
    <a style="left:994px">About Us</a>
    <a style="left:1058px">Contact Us</a>
  </nav>
</div>

</body>
</html>
```